Book Cover Design Project

I have written a booK called "Build From Nothing:
a handbook for launching and steering a modest enterprise. It is aimed at the start up entrepreneur and seeks to give them everything they need to start up and run a small business. I am interested in a very simple cover that is contemporary in the look but clearly communicates the mission of the book. It should sell very well as there are no others like it, so the designer will get excellent exposure.
Updates

Reason: I an vacation in Europe until the 23rd of July. Would like a few days to make a decision after my return Ned

We are currently on vacation.  Will make a final decision in about a week.  Thanks so much for your submissions

Ned

Target Market(s)

Start up businesses in the U.S.

Industry/Entity Type

Business

Requirements
Must have
• Clear communication of the name. Lots of white space. Graphic communication of the purpose of the book? Prominent exposure of my name. Edward r. Kistlewood

```html
<!DOCTYPE html>
<html lang="en">
<head>
<meta charset="utf-8">
<title>Build From Nothing: book cover</title>
<link rel="stylesheet" href="https://fonts.googleapis.com/css2?family=Amatic+SC:wght@700&family=Open+Sans:wght@400&family=Gochi+Hand&display=swap">
<style>
  :root {
    --sunflower: #fec81f;
    --paper: #f4f6f5;
    --white: #ffffff;
    --ink: #231f20;
    --title-font: "Amatic SC", "Arial Narrow", sans-serif;
    --body-font: "Open Sans", Arial, sans-serif;
    --author-font: "Gochi Hand", cursive;
  }
  html, body {
    margin: 0;
    padding: 0;
    width: 1200px;
    height: 758px;
    overflow: hidden;
    background: var(--white);
  }
  .cover-spread {
    position: relative;
    width: 1200px;
    height: 758px;
    background: var(--white);
  }
  .back-cover {
    position: absolute;
    left: 0;
    top: 0;
    width: 530px;
    height: 758px;
    background: var(--sunflower);
  }
  .spine {
    position: absolute;
    left: 548px;
    top: 0;
    width: 105px;
    height: 758px;
    background: var(--sunflower);
  }
  .spine-title {
    position: absolute;
    left: 596px;
    top: 260px;
    margin: 0;
    writing-mode: vertical-rl;
    font-family: var(--title-font);
    font-weight: 700;
    font-size: 42px;
    line-height: 42px;
    color: var(--white);
    white-space: nowrap;
  }
  .spine-subtitle {
    position: absolute;
    left: 555px;
    top: 243px;
    margin: 0;
    writing-mode: vertical-rl;
    font-family: var(--body-font);
    font-size: 11.5px;
    line-height: 16px;
    color: var(--ink);
    white-space: nowrap;
  }
  .spine-author {
    position: absolute;
    left: 548px;
    top: 694px;
    width: 105px;
    margin: 0;
    text-align: center;
    font-family: var(--author-font);
    font-size: 9px;
    color: var(--ink);
    white-space: nowrap;
  }
  .front-cover {
    position: absolute;
    left: 670px;
    top: 0;
    width: 530px;
    height: 758px;
  }
  .front-art {
    display: block;
  }
  .front-title {
    font-family: var(--title-font);
    font-weight: 700;
    font-size: 128px;
  }
  .front-subtitle {
    font-family: var(--body-font);
    font-size: 17px;
  }
  .front-author {
    font-family: var(--author-font);
    font-size: 24px;
    fill: var(--ink);
  }
</style>
</head>
<body>
<main class="cover-spread">
  <section class="back-cover" aria-label="Back cover"></section>

  <section class="spine" aria-label="Spine"></section>
  <h2 class="spine-title">Build From Nothing:</h2>
  <p class="spine-subtitle">a handbook for launching and steering a modest enterprise.</p>
  <p class="spine-author">Edward r. Kistlewood</p>

  <section class="front-cover" aria-label="Front cover">
    <svg class="front-art" width="530" height="758" viewBox="0 0 530 758" xmlns="http://www.w3.org/2000/svg">
      <defs>
        <clipPath id="yellow-field">
          <polygon points="0,0 530,0 530,2 0,752"/>
        </clipPath>
        <clipPath id="pale-field">
          <polygon points="530,2 530,758 0,758 0,752"/>
        </clipPath>
        <linearGradient id="case-tone" x1="0" y1="0" x2="1" y2="1">
          <stop offset="0" stop-color="#2c292a"/>
          <stop offset="1" stop-color="#1a1818"/>
        </linearGradient>
      </defs>

      <rect class="field-sunflower" width="530" height="758" fill="var(--sunflower)"/>
      <polygon class="field-paper" points="530,2 530,758 0,758 0,752" fill="var(--paper)"/>

      <g class="front-title">
        <text x="50" y="205" textLength="440" lengthAdjust="spacingAndGlyphs" fill="var(--white)" clip-path="url(#yellow-field)">Build From Nothing:</text>
        <text x="50" y="205" textLength="440" lengthAdjust="spacingAndGlyphs" fill="var(--sunflower)" clip-path="url(#pale-field)">Build From Nothing:</text>
      </g>

      <g class="front-subtitle">
        <text x="40" y="244" textLength="465" lengthAdjust="spacingAndGlyphs" fill="var(--white)" clip-path="url(#yellow-field)">a handbook for launching and steering a modest enterprise.</text>
        <text x="40" y="244" textLength="465" lengthAdjust="spacingAndGlyphs" fill="var(--sunflower)" clip-path="url(#pale-field)">a handbook for launching and steering a modest enterprise.</text>
      </g>

      <rect class="cover-illustration" x="170" y="380" width="220" height="240" rx="6" fill="url(#case-tone)" role="img" aria-label="Illustration of a briefcase with a sprout growing from it, leaves labelled new business"/>

      <text class="front-author" x="340" y="718" textLength="180" lengthAdjust="spacingAndGlyphs">Edward r. Kistlewood</text>
    </svg>
  </section>
</main>
</body>
</html>
```